Letterhead needed using basic elements of our new logo!

We have just had a new logo and business card created on Pixel Harbor and now would like a new letterhead for our company re-branding. Our logo inspires trust, professionalism and confidence and we would like to mirror that in our letterhead. We would like to use elements in our logo (as well as the logo itself, obviously), but understand with only a header and the ability to print in black and white, we are somewhat limited. We have also won the Resident's Pick Medal for best Property Management Company in our city and would like to somehow include that small banner (see uploaded file) in the letterhead, without it clashing?

Text to include:
Stonebrook Property Management (and logo)
C-214 Marlowe Ave, Winnipeg, MB R2K 3P7
Ph: 204-738-2915
Fax: 1-888-276-9413
Email: customerservice@stonebrookpropertymanagement.example
Web: www.stonebrookpropertymanagement.example

Pasted below is our mission, vision and branding statements to help with the project:

Mission Statement

Provide the highest quality customer service to both property owners and tenants using innovative technology and well trained, caring staff.

Vision Statement

To redefine the way in which management is delivered to its customers, becoming the recognized leader in the property management industry.

Brand Essence

When our customers experience our product or service, it brings forth an emotion of absolute trust that we have their best interests at heart

Brand Personality

We are a company that is passionate about our customers, our company and our vision to be leaders in the field of property management. We are visionaries that aren't afraid to use cutting edge technologies to improve our products and service.

Position or Value Proposition

To whom are we speaking?
- real estate investors, including first timers that are giving us their first starter home. They are fairly naive, as they are not "big time" investors, and because they are giving us their first home (in contract to an investor buying a rental property, often sight unseen) they are more emotionally tied to their property and will require a company that inspires trust and confidence.

What is our brand promise?
- we will do our best to serve our clients, both owners and tenants, to give them prompt communication, clear, concise answers to their questions, and look after their property quickly and competently.

Why is our product different than the competition and why should our customers care?
- the current model used by most management companies employs individual portfolio managers that do things a little differently each instance, and differently than their fellow staff members. Our management product is superior because we use a combination of technology and strict procedures to ensure each client's experience is consistent, each and every time.

Industry/Entity Type

Business

Requirements
Must have
• We would like an option to be in black and white, to be able to be printed from Microsoft Word. As well, we do not want anything in a footer or any other kind of letterhead that bleeds below a header. The main use of this letterhead will be from our property management software, to be used in our form letters and other templates (sent to tenants and clients)
Should not have
• Footer or other elements where the text body would be, it will be used in a form letter

```html
<!DOCTYPE html>
<html lang="en">
<head>
<meta charset="utf-8">
<title>Stonebrook Property Management – Letterhead</title>
<link href="https://fonts.googleapis.com/css2?family=Source+Sans+3:wght@400;600;700&display=swap" rel="stylesheet">
<style>
  :root {
    --backdrop: #bac9c0;
    --paper: #ffffff;
    --brand-blue: #1a6fb5;
    --ink: #2a1a1a;
    --medal: #d8dde3;
  }
  * { margin: 0; padding: 0; box-sizing: border-box; }
  html, body {
    width: 1200px; height: 1200px; overflow: hidden;
    background: var(--backdrop);
    font-family: "Source Sans 3", Arial, sans-serif;
  }
  .letterhead {
    position: absolute; left: 189px; top: 0;
    width: 853px; height: 1200px;
    background: var(--paper);
  }
  .rule {
    position: absolute; top: 78px; height: 3px;
    background: var(--brand-blue);
  }
  .rule--left { left: 0; width: 61px; }
  .rule--right { left: 293px; right: 0; }
  .brand {
    position: absolute; left: 69px; top: 60px;
    display: flex; align-items: center; gap: 8px;
  }
  .brand__mark { width: 36px; height: 36px; background: var(--brand-blue); }
  .brand__name {
    color: var(--brand-blue);
    font-weight: 700;
    font-size: 15px;
    line-height: 16px;
    letter-spacing: 0.5px;
    text-transform: uppercase;
  }
  .award-medal {
    position: absolute; left: 330px; top: 22px;
    width: 44px; height: 44px; border-radius: 50%;
    background: var(--medal);
    border: 2px solid var(--brand-blue);
  }
  .contact {
    position: absolute; right: 60px; top: 14px;
    text-align: right;
    color: var(--ink);
    font-style: normal;
    font-size: 11.5px;
    line-height: 14px;
    letter-spacing: -0.1px;
  }
  .contact__phones { display: flex; justify-content: flex-end; align-items: center; gap: 3px; }
  .contact__icon { width: 9px; height: 9px; fill: var(--ink); }
  .contact__sep { margin: 0 1px; }
</style>
</head>
<body>
  <div class="letterhead">
    <div class="rule rule--left"></div>
    <div class="rule rule--right"></div>

    <div class="brand">
      <div class="brand__mark"></div>
      <div class="brand__name">Stonebrook<br>Property Management</div>
    </div>

    <div class="award-medal" role="img" aria-label="Resident's Pick Medal badge"></div>

    <address class="contact">
      <div class="contact__phones">
        <svg class="contact__icon" viewBox="0 0 10 10" aria-label="Mobile"><path d="M3 0h4a1 1 0 0 1 1 1v8a1 1 0 0 1-1 1H3a1 1 0 0 1-1-1V1a1 1 0 0 1 1-1zm0 1.5v6h4v-6z"/></svg>
        <span>204-738-2915</span><span class="contact__sep">|</span>
        <svg class="contact__icon" viewBox="0 0 10 10" aria-label="Phone"><rect width="10" height="10" rx="2"/><path d="M3 2.2l1.2 1.3-.6.8c.4.9 1.1 1.6 2 2l.8-.6L7.8 7 7 7.9C4.6 7.5 2.5 5.4 2.1 3z" fill="#fff"/></svg>
        <span>204-738-2948</span><span class="contact__sep">|</span>
        <svg class="contact__icon" viewBox="0 0 10 10" aria-label="Fax"><path d="M2.5 0h5v3h-5zM0 3.5h10v4.5H8V6H2v2H0zM2.5 6.5h5V10h-5z"/></svg>
        <span>1-888-276-9413</span>
      </div>
      <div>customerservice@stonebrookpropertymanagement.example</div>
      <div>www.stonebrookpropertymanagement.example</div>
      <div>C-214 Marlowe Ave, Winnipeg, Manitoba R2K 3P7</div>
    </address>
  </div>
</body>
</html>
```